Take Out Menu

We are looking to redo our take out menu.
See current attached file for our current design.
The menu should make you hungry when looking at the pictures.
Target Market(s)
All of our customers.
Industry/Entity Type
Restaurant
Contact Information for Business Card
I will attach an image of our current card. It has the details of what we need on it.
Colors
Designer to choose colors to be used in the design.
Requirements
Must have
- A fresh look and feel. We must use our current logo branding. You can look at Melvoras on google to see what our restaurants look like.
Nice to have
- Easy read with food pictures.

```html
<!DOCTYPE html>
<html lang="en">
<head>
<meta charset="utf-8">
<title>Melvoras Take Out Menu</title>
<link rel="stylesheet" href="https://fonts.googleapis.com/css2?family=Anton&family=Open+Sans:wght@400;600;700&display=swap">
<style>
  :root {
    --page-bg: #e9e6e1;
    --paper: #f3efe8;
    --paper-fold: #ebe6dd;
    --brand-red: #b01f24;
    --ink: #2a2624;
    --ink-soft: #3d3835;
    --white: #ffffff;
    --dark-red: #5a1012;
  }
  * { box-sizing: border-box; margin: 0; padding: 0; }
  html, body { width: 1200px; height: 880px; overflow: hidden; }
  body {
    background: var(--page-bg);
    font-family: "Open Sans", Arial, sans-serif;
    color: var(--ink);
    position: relative;
  }
  .menu {
    position: absolute; left: 66px; top: 22px;
    width: 1068px; height: 836px;
    background: var(--paper);
    box-shadow: 0 4px 14px rgba(0,0,0,.18);
    overflow: hidden;
  }
  .fold {
    position: absolute; top: 0; bottom: 0; width: 332px; left: 366px;
    background: var(--paper-fold);
  }
  .abs { position: absolute; }
  .section-title {
    font-family: "Anton", Impact, sans-serif;
    color: var(--brand-red);
    font-weight: 400;
    letter-spacing: .5px;
    line-height: 1;
  }
  .price-list { list-style: none; font-size: 13px; font-weight: 700; }
  .price-list li { display: flex; align-items: baseline; height: 16px; line-height: 16px; }
  .price-list .name { white-space: nowrap; }
  .price-list .dots { flex: 1; border-bottom: 1.5px dotted var(--ink); margin: 0 4px 4px 2px; }
  .price-list .price { width: 48px; text-align: left; }
  .note { font-size: 12px; font-weight: 400; color: var(--ink-soft); text-align: center; line-height: 17px; }
  .sub { font-size: 12px; font-weight: 400; color: var(--ink-soft); line-height: 13px; padding-left: 42px; }

  .photo { position: absolute; border-radius: 50%; }
  .photo-doubles {
    left: 316px; top: 54px; width: 394px; height: 240px;
    border-radius: 48% 52% 44% 56% / 58% 52% 48% 42%;
    background: radial-gradient(ellipse at 45% 55%, #c48a3d 0%, #e0b463 45%, #d9b07a 70%, #f2efe9 100%);
  }
  .photo-roti {
    left: 4px; top: 380px; width: 206px; height: 134px;
    background: radial-gradient(ellipse at 50% 50%, #9b6a2e 0%, #d38a3a 40%, #e8e2d2 75%, #f4f2ee 100%);
  }
  .photo-plate {
    left: 764px; top: 410px; width: 238px; height: 230px; border-radius: 6px;
    background: radial-gradient(circle at 55% 45%, #5a2a16 0%, #8a5a2c 40%, #b79a6a 65%, #eef0ea 100%);
    box-shadow: 0 3px 8px rgba(0,0,0,.2);
  }

  .table { font-size: 12.5px; font-weight: 700; border-collapse: collapse; }
  .table td { height: 16px; line-height: 16px; padding: 0; }
  .table th { font-size: 12px; font-weight: 400; height: 30px; vertical-align: top; text-align: left; }
  .table .item { width: 162px; white-space: nowrap; }
  .table .sm { width: 60px; }

  .specials-box {
    left: 710px; top: 102px; width: 344px; height: 354px;
    background: var(--brand-red); color: var(--white);
  }
  .specials-box .call {
    font-family: "Anton", Impact, sans-serif; text-align: center; line-height: 1;
  }
  .specials-box .info { font-weight: 700; font-size: 19px; }
  .specials-box .phone { font-weight: 400; font-size: 25px; margin-left: 6px; }
  .size-tag { color: var(--dark-red); }

  .daily-band {
    left: 0; top: 754px; width: 334px; height: 32px;
    background: var(--brand-red); color: var(--white);
    font-weight: 600; font-size: 15.5px; line-height: 32px; padding-left: 52px;
  }
  .brand {
    left: 730px; top: 690px; font-weight: 700; font-size: 22px; color: var(--brand-red);
    display: flex; align-items: center; gap: 6px;
  }
  .brand-dot { width: 12px; height: 12px; border-radius: 50%; background: var(--brand-red); }
</style>
</head>
<body>
<main class="menu">
  <div class="fold"></div>

  <!-- Panel one -->
  <h2 class="section-title abs" style="left:183px;top:46px;font-size:29px;">APPETIZERS</h2>
  <ul class="price-list abs" style="left:58px;top:88px;width:252px;">
    <li><span class="name">Doubles</span><span class="dots"></span><span class="price">$2.25</span></li>
    <li><span class="name">Gourmet Doubles</span><span class="dots"></span><span class="price">$4.49</span></li>
    <li class="note" style="height:12px;line-height:12px;padding-left:12px;">Chicken, Goat, Shrimp</li>
    <li><span class="name">Aloo Pie</span><span class="dots"></span><span class="price">$2.49</span></li>
    <li><span class="name">Sahiena</span><span class="dots"></span><span class="price">$2.49</span></li>
    <li><span class="name">Phulourie (10)</span><span class="dots"></span><span class="price">$2.99</span></li>
  </ul>
  <p class="note abs" style="left:70px;top:186px;width:250px;">W/tamarind or other choice of sauce<br>With channa add $0.50<br>With Meat add $3.00</p>

  <h2 class="section-title abs" style="left:60px;top:244px;font-size:28px;">PLAIN ROTI</h2>
  <ul class="price-list abs" style="left:57px;top:286px;width:254px;">
    <li><span class="name">Dhalpurie</span><span class="dots"></span><span class="price">$2.99</span></li>
    <li><span class="name">Paratha</span><span class="dots"></span><span class="price">$2.99</span></li>
    <li><span class="name">Sada</span><span class="dots"></span><span class="price">$2.99</span></li>
    <li><span class="name">Bake</span><span class="dots"></span><span class="price">$2.99</span></li>
    <li><span class="name">Wedding/Party Size</span><span class="dots"></span><span class="price">$13.99</span></li>
  </ul>
  <p class="note abs" style="left:70px;top:368px;width:210px;">Please ask if available</p>

  <div class="photo photo-roti" role="img" aria-label="Plate of roti with curried vegetables, greens and a scotch bonnet pepper"></div>

  <h2 class="section-title abs" style="left:215px;top:483px;font-size:28px;">Rice Dishes</h2>
  <ul class="price-list abs" style="left:46px;top:530px;width:278px;">
    <li><span class="name">Stew Chicken</span><span class="dots"></span><span class="price">$12.99</span></li>
    <li class="sub">served with calallo</li>
    <li style="margin-top:6px;"><span class="name">Jerk Chicken</span><span class="dots"></span><span class="price">$13.49</span></li>
    <li class="sub">served with Rice &amp; Peas</li>
    <li style="margin-top:10px;"><span class="name">Curry King Fish&nbsp;</span><span class="dots"></span><span class="price">$15.99</span></li>
    <li style="margin-top:13px;"><span class="name">Bake</span><span class="dots"></span><span class="price">$5.99</span></li>
    <li class="sub" style="padding-left:32px;">with Smoked Harring or Saltfish</li>
    <li style="margin-top:8px;"><span class="name">Bake &amp; Shark</span><span class="dots"></span><span class="price">$12.99</span></li>
  </ul>

  <div class="daily-band abs">Inquire about our daily specials!</div>

  <!-- Panel two -->
  <div class="photo photo-doubles" role="img" aria-label="Platter of doubles, aloo pie, phulourie and saheena with tamarind sauce"></div>

  <h2 class="section-title abs" style="left:427px;top:388px;font-size:27px;">RICE/ROTI DISHES</h2>
  <table class="table abs" style="left:403px;top:428px;">
    <tr><th></th><th class="sm">&nbsp;SM.</th><th>LRG.</th></tr>
    <tr><td class="item">Bone-in Chicken..........</td><td>$8.99</td><td>$10.49</td></tr>
    <tr><td class="item">Boneless Chicken......</td><td>$9.99</td><td>$11.99</td></tr>
    <tr><td class="item">Bone-in Goat................</td><td>$8.99</td><td>$10.99</td></tr>
    <tr><td class="item">Boneless Goat............</td><td>$10.49</td><td>$12.49</td></tr>
    <tr><td class="item">Shrimp............................</td><td>$10.99</td><td>$12.99</td></tr>
    <tr><td class="item">Duck..............................</td><td>$1099</td><td>$12.99</td></tr>
    <tr><td class="item">Stew Chicken.............</td><td>$8.49</td><td>$10.49</td></tr>
    <tr><td class="item">Pachouni......................</td><td>$9.99</td><td>$11.99</td></tr>
  </table>
  <p class="abs" style="left:470px;top:636px;width:230px;text-align:center;font-size:13px;font-weight:600;line-height:18px;">Served with choice of dhal,<br>patato, or channa</p>
  <table class="table abs" style="left:428px;top:706px;">
    <tr><td class="item" style="width:164px;">Veggie (4 items)...........</td><td>$13.99</td></tr>
    <tr><td class="item" style="width:164px;">Potato/Channa.........</td><td>$9.99</td></tr>
  </table>

  <!-- Panel three -->
  <h1 class="section-title abs" style="left:735px;top:40px;font-size:58px;">Specials</h1>
  <section class="specials-box abs">
    <p class="call" style="margin-top:34px;font-size:31px;">Please Call for</p>
    <p class="call" style="margin-top:4px;font-size:40px;">DAILY SPECIALS</p>
    <p class="info" style="margin:20px 0 0 74px;">Trini Special&nbsp;&nbsp;&nbsp;&nbsp;$4.00</p>
    <p class="info" style="margin:18px 0 0 52px;">Ajax<span class="phone">905.555.0142</span></p>
    <p class="info" style="margin:2px 0 0 52px;">Toronto<span class="phone">416.555.0187</span></p>
    <p class="info" style="margin:26px 0 0 42px;">Fish Broth&nbsp;&nbsp;<span class="size-tag">M</span> $5.50 <span class="size-tag">L</span>$6.50</p>
  </section>

  <div class="photo photo-plate" role="img" aria-label="Jerk chicken with rice and peas, tomato, cucumber and lettuce"></div>

  <div class="brand abs"><span class="brand-dot"></span>Melvoras</div>
  <p class="section-title abs" style="left:859px;top:688px;font-size:28px;">VISIT US ONLINE!</p>
  <p class="abs" style="left:860px;top:724px;font-size:17px;font-weight:700;color:var(--ink-soft);">www.melvoras.com</p>
</main>
</body>
</html>
```